Photography Business, Business Card

Looking for a unique cutting edge card that takes advantage of the latest printing technologies. Please review this site for all the options they office: https://plumeprints.example. If you can think it they can do it. And if you have an idea and do not know if they can do it, I will check into it.
Updates

Target Market(s)

People and places I took images of and future clients.

Industry/Entity Type

Photography

Contact Information for Business Card

Name, cell & email. Colin Hartley, chartley@kvnphoto.example, 318-742-9061

Colors

Designer to choose only greyscale colors for use in the design.

Requirements
Must have
• 100% cutting edge. Is so great, those I hand it to always show it to someone else. A piece of art.
Nice to have
• Blacks, silvers, greys, some red. Maybe other colors?

```html
<!DOCTYPE html>
<html lang="en">
<head>
<meta charset="utf-8">
<title>Colin Hartley Photography – Business Card</title>
<link href="https://fonts.googleapis.com/css2?family=Poppins:wght@400;600;700&display=swap" rel="stylesheet">
<style>
  :root {
    --page: #ffffff;
    --card: #232323;
    --ink: #ffffff;
    --accent: #e02127;
    --ghost: #2b2b2b;
    --shadow: rgba(0,0,0,0.28);
  }
  * { margin: 0; padding: 0; box-sizing: border-box; }
  html, body { width: 692px; height: 1200px; overflow: hidden; background: var(--page); }
  body { position: relative; font-family: "Poppins", sans-serif; color: var(--ink); }

  .card {
    position: absolute; left: 104px; width: 484px; height: 277px;
    background: var(--card); overflow: hidden;
    box-shadow: 0 14px 40px var(--shadow);
  }
  .card--front { top: 300px; }
  .card--back { top: 624px; }

  .viewfinder { position: absolute; inset: 0; width: 100%; height: 100%; }
  .ghost-ring { position: absolute; border-radius: 50%; border: 18px solid var(--ghost); }
  .card--front .ghost-ring { left: 128px; top: 22px; width: 232px; height: 232px; }
  .card--back .ghost-ring { left: 280px; top: -10px; width: 300px; height: 300px; }

  .hud { position: absolute; font-weight: 700; font-size: 9px; line-height: 1; }
  .hud-res { left: 26px; top: 25px; display: flex; gap: 4px; align-items: center; }
  .hud-res .badge { background: var(--ink); color: var(--card); border-radius: 3px; padding: 1px 4px; }
  .hud-raw { left: 24px; top: 43px; border: 1.4px solid var(--ink); border-radius: 3px; padding: 1px 7px; }
  .hud-battery { right: 28px; top: 25px; display: flex; gap: 5px; align-items: center; font-weight: 400; }
  .hud-grid { left: 33px; top: 197px; }
  .hud-fps { left: 32px; top: 234px; font-weight: 600; letter-spacing: 1px; }
  .hud-rec { left: 31px; top: 246px; display: flex; align-items: center; gap: 2px; }
  .hud-rec .dot { width: 8px; height: 8px; border-radius: 50%; background: var(--accent); }
  .hud-auto { right: 56px; top: 248px; font-weight: 600; letter-spacing: 1px; }
  .hud-flash { right: 30px; top: 236px; }

  .name { position: absolute; font-weight: 400; color: var(--ink); white-space: nowrap; }
  .tagline { position: absolute; font-weight: 400; letter-spacing: 3px; white-space: nowrap; }
  .brand { position: absolute; font-weight: 700; color: var(--accent); white-space: nowrap; letter-spacing: 10px; line-height: 1; }

  .card--front .name { left: 96px; top: 84px; font-size: 36px; }
  .card--front .tagline { left: 284px; top: 143px; font-size: 10px; }
  .card--front .brand { left: 172px; top: 170px; font-size: 44px; }

  .card--back .brand { left: 72px; top: 59px; font-size: 44px; }
  .card--back .name { left: 73px; top: 109px; font-size: 20px; }
  .card--back .tagline { left: 74px; top: 134px; font-size: 6px; letter-spacing: 2px; }

  .contact { position: absolute; left: 73px; display: flex; align-items: center; gap: 12px; font-weight: 700; }
  .contact--phone { top: 160px; font-size: 19px; }
  .contact--email { top: 200px; font-size: 12px; font-weight: 600; }
  .contact svg { flex: none; }
</style>
</head>
<body>

<section class="card card--front" aria-label="Business card front">
  <div class="ghost-ring"></div>
  <svg class="viewfinder" viewBox="0 0 484 277" fill="none" stroke="#fff" stroke-width="1">
    <path d="M17 108V16H108M376 16H467V108M17 169V261H108M376 261H467V169"/>
  </svg>
  <div class="hud hud-res"><span>HD</span><span class="badge">4K</span><span>8K</span></div>
  <div class="hud hud-raw">RAW</div>
  <div class="hud hud-battery">
    <svg width="26" height="11" viewBox="0 0 26 11"><rect x="2" y="0.7" width="23" height="9.6" fill="none" stroke="#fff" stroke-width="1.2"/><rect x="0" y="3" width="2" height="5" fill="#fff"/><rect x="5" y="3" width="14" height="5" fill="#fff"/></svg>
    <span>72%</span>
  </div>
  <svg class="hud hud-grid" width="18" height="18" viewBox="0 0 18 18" fill="none" stroke="#fff" stroke-width="1"><path d="M1 1H17V17H1ZM1 6.3H17M1 11.6H17M6.3 1V17M11.6 1V17M1 1L17 17"/></svg>
  <div class="hud hud-fps">30 FPS</div>
  <div class="hud hud-rec"><span class="dot"></span><span>REC</span></div>
  <div class="hud hud-auto">AUTO</div>
  <svg class="hud hud-flash" width="16" height="22" viewBox="0 0 16 22" fill="#fff"><path d="M9 0L2 12H7L5 22L14 9H9Z"/><path d="M1 3L15 19" stroke="#fff" stroke-width="1.2"/></svg>

  <div class="name">Colin Hartley</div>
  <div class="tagline">PHOTOGRAPHY</div>
  <div class="brand">KVN</div>
</section>

<section class="card card--back" aria-label="Business card back">
  <div class="ghost-ring"></div>
  <svg class="viewfinder" viewBox="0 0 484 277" fill="none" stroke="#fff" stroke-width="1">
    <path d="M17 108V16H108M376 16H467V108M17 169V261H108M376 261H467V169"/>
  </svg>
  <div class="hud hud-res"><span>HD</span><span class="badge">4K</span><span>8K</span></div>
  <div class="hud hud-raw">RAW</div>
  <div class="hud hud-battery">
    <svg width="26" height="11" viewBox="0 0 26 11"><rect x="2" y="0.7" width="23" height="9.6" fill="none" stroke="#fff" stroke-width="1.2"/><rect x="0" y="3" width="2" height="5" fill="#fff"/><rect x="5" y="3" width="14" height="5" fill="#fff"/></svg>
    <span>72%</span>
  </div>
  <svg class="hud hud-grid" width="18" height="18" viewBox="0 0 18 18" fill="none" stroke="#fff" stroke-width="1"><path d="M1 1H17V17H1ZM1 6.3H17M1 11.6H17M6.3 1V17M11.6 1V17M1 1L17 17"/></svg>
  <div class="hud hud-fps">30 FPS</div>
  <div class="hud hud-rec"><span class="dot"></span><span>REC</span></div>
  <div class="hud hud-auto">AUTO</div>
  <svg class="hud hud-flash" width="16" height="22" viewBox="0 0 16 22" fill="#fff"><path d="M9 0L2 12H7L5 22L14 9H9Z"/><path d="M1 3L15 19" stroke="#fff" stroke-width="1.2"/></svg>

  <div class="brand">KVN</div>
  <div class="name">Colin Hartley</div>
  <div class="tagline">PHOTOGRAPHY</div>

  <div class="contact contact--phone">
    <svg width="18" height="18" viewBox="0 0 24 24" fill="#e02127"><path d="M6.6 10.8a15.1 15.1 0 006.6 6.6l2.2-2.2a1 1 0 011-.25 11.4 11.4 0 003.6.57 1 1 0 011 1V20a1 1 0 01-1 1A17 17 0 013 4a1 1 0 011-1h3.5a1 1 0 011 1 11.4 11.4 0 00.57 3.6 1 1 0 01-.25 1z"/></svg>
    <span>318-742-9061</span>
  </div>
  <div class="contact contact--email">
    <svg width="18" height="13" viewBox="0 0 18 13" fill="#e02127"><path d="M0 0H18V1.5L9 7 0 1.5Z"/><path d="M0 3.3L9 8.8 18 3.3V13H0Z"/></svg>
    <span>chartley@kvnphoto.example</span>
  </div>
</section>

</body>
</html>
```